Digital One Pager for Consulting Practice

I would like the essence of the content in my ppt consolidated into a one-pager. The one-pager will mainly be sent via email as a pdf and intended to excite and invite new clients and establish the credibility of my boutique high-end consulting firm. Infographics and symbols would be a plus. The target client should view the firm as providing premeir service. The client is getting a thought partner.

Target Market(s)

Large Medical Device Manufacturer Executives, Early-Stage Medical Device Manufacturer Executives, Partners at VC Firms

Industry/Entity Type

Medical Equipment

Colors
0355a3
f37122

Requirements
Must have
• Please match the color scheme in ppt. Please use the existing logo. I am very open to better graphics on the process. My photo does not need to be on the digital flyer. Hyper link to the website and email is needed.
Nice to have
• Infographics

```html
<!DOCTYPE html>
<html lang="en">
<head>
<meta charset="utf-8">
<title>Halvern Advisory – One Pager</title>
<link rel="stylesheet" href="https://fonts.googleapis.com/css2?family=Montserrat:wght@500;600;700;800&family=Open+Sans:wght@400;600;700&display=swap">
<style>
:root{
  --blue:#0355a3;
  --blue-deep:#03437f;
  --orange:#f37122;
  --ink:#1d2a3a;
  --gray:#6b6f75;
  --white:#ffffff;
  --backdrop:#e8e9eb;
}
*{margin:0;padding:0;box-sizing:border-box}
html,body{width:880px;height:1200px;overflow:hidden;background:var(--backdrop)}
body{position:relative;font-family:"Open Sans",Arial,sans-serif;color:var(--ink)}
.page{position:absolute;top:303px;width:420px;height:594px;background:var(--white);overflow:hidden;box-shadow:0 6px 18px rgba(0,0,0,.18)}
.page--front{left:14px}
.page--back{left:446px}
.abs{position:absolute}
.photo{position:absolute;background:linear-gradient(135deg,#dfe7ef 0%,#b9c6d4 45%,#6d7f93 100%)}
.photo--warm{background:linear-gradient(135deg,#f1ece6 0%,#cdb9a6 50%,#6b5a4c 100%)}
.photo--dark{background:linear-gradient(135deg,#5b4236 0%,#2e2622 100%)}
.heading{font-family:"Montserrat",Arial,sans-serif;font-weight:700}
.list{list-style:none}
.list li{position:relative;padding-left:9px;line-height:1.32;margin-bottom:3px}
.list li::before{content:"";position:absolute;left:0;top:3.5px;width:4px;height:4px;border-radius:50%;border:1px solid var(--orange)}
/* front */
.logo{left:18px;top:286px}
.logo__name{font-family:"Montserrat",Arial,sans-serif;font-weight:800;font-size:27px;letter-spacing:1px;color:var(--ink);line-height:1}
.logo__sub{font-family:"Montserrat",Arial,sans-serif;font-weight:800;font-size:11px;letter-spacing:5.2px;color:var(--ink);margin-top:2px}
.provide{left:128px;top:338px;width:110px;font-size:7px}
.provide__title{font-size:9px;color:var(--blue);margin-bottom:1px}
.provide__sub{font-family:"Montserrat",Arial,sans-serif;font-weight:600;font-size:7.5px;color:var(--orange);margin:4px 0 3px}
.experience{left:254px;top:238px;width:150px;font-size:6.8px;color:var(--white)}
.experience__title{font-size:12px;color:var(--orange);margin-bottom:5px}
.experience .list li::before{border-color:var(--white)}
.contact{font-family:"Montserrat",Arial,sans-serif;font-weight:600;color:var(--white);font-size:9px;display:flex;align-items:center;gap:5px}
.contact a{color:var(--white);text-decoration:none}
.web{font-family:"Montserrat",Arial,sans-serif;font-weight:600;font-size:10px;letter-spacing:1.4px;color:var(--white);text-decoration:none}
/* back */
.services{left:14px;top:306px;width:180px;color:var(--white)}
.services__title{font-size:13px;margin-bottom:8px}
.service{display:flex;gap:8px;margin-bottom:7px;align-items:flex-start}
.service__thumb{flex:0 0 52px;height:44px;border:2px solid var(--white);border-radius:3px}
.service__name{font-family:"Montserrat",Arial,sans-serif;font-weight:600;font-size:7.5px;color:var(--orange);margin-bottom:2px}
.service .list{font-size:6.8px}
.service .list li{margin-bottom:1px}
.service .list li::before{border-color:var(--white)}
.section-title{font-size:10px;color:var(--ink)}
.step{position:absolute;width:48px;height:30px;color:var(--white);font-family:"Montserrat",Arial,sans-serif;font-weight:600;font-size:6.3px;line-height:1.15;display:flex;align-items:center;justify-content:center;text-align:center;padding:0 8px 0 10px;clip-path:polygon(0 0,85% 0,100% 50%,85% 100%,0 100%,15% 50%)}
.step--blue{background:var(--blue)}
.step--orange{background:var(--orange)}
.partner{position:absolute;background:#d9dee5;border-radius:3px}
</style>
</head>
<body>

<!-- FRONT SIDE -->
<section class="page page--front">
  <div class="photo" style="left:0;top:0;width:420px;height:290px" role="img" aria-label="Photo of executives meeting around a table in a bright office"></div>

  <svg class="abs" style="left:0;top:0" width="420" height="594" viewBox="0 0 420 594" aria-hidden="true">
    <path d="M412 140 L420 140 L420 594 L0 594 L0 566 L412 566 Z" fill="var(--orange)"/>
    <path d="M262 212 H412 V566 H0 V530 H218 Q240 530 240 508 V234 Q240 212 262 212 Z" fill="var(--blue)"/>
    <path d="M0 270 H240 V508 Q240 530 218 530 H0 Z" fill="var(--white)"/>
  </svg>

  <div class="abs" style="left:300px;top:118px;width:104px;height:104px;border-radius:50%;border:4px solid var(--white);background:linear-gradient(135deg,#c9ccd2,#5a5e66);box-shadow:0 2px 6px rgba(0,0,0,.25)" role="img" aria-label="Portrait of the firm's founder"></div>

  <div class="abs logo">
    <div class="logo__name">HALVERN</div>
    <div class="logo__sub" style="color:var(--orange)">ADVISORY</div>
  </div>

  <div class="photo" style="left:14px;top:378px;width:104px;height:118px;border:3px solid var(--orange);border-radius:4px" role="img" aria-label="Photo of two businessmen shaking hands in an office"></div>

  <div class="abs provide">
    <div class="heading provide__title">Experience to Provide...</div>
    <div class="provide__sub">Executive Application Review</div>
    <ul class="list">
      <li>Examples include: Presubmission, IDE, 510(k), PMA, Refuse to Accept, Hold letter</li>
      <li>Troubleshooting</li>
    </ul>
    <div class="provide__sub">Strategic Advice &amp; Diligence to Investors</div>
    <ul class="list">
      <li>Validate &amp; Verify Founder Milestones</li>
      <li>Diligence portfolio company Regulatory and Quality systems</li>
    </ul>
  </div>

  <div class="abs experience">
    <div class="heading experience__title">Experience</div>
    <ul class="list">
      <li>Over a decade @FDA (Former Deputy Division Director)</li>
      <li>Expertise: Cardiovascular, Ophthalmology, General Hospital, Infection Control, Dental, Anesthesia, Respiratory</li>
      <li>Vice President Regulatory Affairs / Quality Assurance @Corvane (Fortune 150 Company)</li>
      <li>Initiated reorganization of department</li>
      <li>Led major compliance effort</li>
      <li>Successful FDA inspection (no observations)</li>
    </ul>
  </div>

  <div class="abs contact" style="left:16px;top:541px">
    <svg width="10" height="10" viewBox="0 0 24 24" aria-hidden="true"><circle cx="12" cy="12" r="11" fill="none" stroke="#fff" stroke-width="2"/><path d="M8 6l2 0 1 3-1.5 1a7 7 0 0 0 3.5 3.5l1-1.5 3 1v2a2 2 0 0 1-2 2A10 10 0 0 1 6 8a2 2 0 0 1 2-2z" fill="#fff"/></svg>
    <a href="tel:5550142290">555.014.2290</a>
  </div>
  <div class="abs contact" style="left:236px;top:541px;font-size:7.5px">
    <svg width="10" height="10" viewBox="0 0 24 24" aria-hidden="true"><circle cx="12" cy="12" r="11" fill="none" stroke="#fff" stroke-width="2"/><rect x="6" y="8" width="12" height="8" fill="none" stroke="#fff" stroke-width="1.6"/><path d="M6 8l6 5 6-5" fill="none" stroke="#fff" stroke-width="1.6"/></svg>
    <a href="mailto:info@halvernadvisory.com">info@halvernadvisory.com</a>
  </div>
  <a class="abs web" href="https://www.halvernadvisory.com" style="right:14px;top:572px">www.halvernadvisory.com</a>
</section>

<!-- BACK SIDE -->
<section class="page page--back">
  <div class="photo photo--warm" style="left:0;top:0;width:420px;height:300px" role="img" aria-label="Photo of a team collaborating around a conference table"></div>

  <svg class="abs" style="left:0;top:0" width="420" height="594" viewBox="0 0 420 594" aria-hidden="true">
    <path d="M0 280 Q150 260 420 250 V594 H0 Z" fill="var(--white)"/>
    <path d="M0 292 H8 V566 H420 V594 H0 Z" fill="var(--orange)"/>
    <path d="M8 300 H182 Q204 300 204 322 V514 Q204 536 226 536 H412 V566 H8 Z" fill="var(--blue)"/>
  </svg>

  <div class="abs services">
    <div class="heading services__title">Services</div>
    <div class="service">
      <div class="service__thumb" style="background:#f4f6f9" role="img" aria-label="Simple regulatory pathway flow diagram"></div>
      <div><div class="service__name">Regulatory Strategy</div>
        <ul class="list"><li>RA/QA Organizational Structure</li><li>Regulatory Pathway</li></ul></div>
    </div>
    <div class="service">
      <div class="service__thumb photo" style="position:static" role="img" aria-label="Photo of hands reviewing documents"></div>
      <div><div class="service__name">FDA Communications</div>
        <ul class="list"><li>Deficiency Response</li><li>Application Review</li></ul></div>
    </div>
    <div class="service">
      <div class="service__thumb photo photo--warm" style="position:static" role="img" aria-label="Photo of an executive speaking at a meeting"></div>
      <div><div class="service__name">Interim Executive Leadership</div>
        <ul class="list"><li>Compliance Remediation</li><li>Accelerated Product Registration</li></ul></div>
    </div>
    <div class="service">
      <div class="service__thumb photo photo--dark" style="position:static" role="img" aria-label="Photo of a training session audience"></div>
      <div><div class="service__name">Training</div>
        <ul class="list"><li>FDA Communication</li><li>MDR Reporting</li></ul></div>
    </div>
  </div>

  <div class="abs heading section-title" style="left:216px;top:272px">Differentiators</div>
  <svg class="abs" style="left:252px;top:288px" width="130" height="130" viewBox="0 0 130 130" role="img" aria-label="Leverage cycle: network, process, experience">
    <g transform="rotate(-210 65 65)" fill="none" stroke-width="26">
      <circle cx="65" cy="65" r="44" stroke="var(--blue)" stroke-dasharray="88 188"/>
    </g>
    <g transform="rotate(-90 65 65)" fill="none" stroke-width="26">
      <circle cx="65" cy="65" r="44" stroke="var(--orange)" stroke-dasharray="88 188"/>
    </g>
    <g transform="rotate(30 65 65)" fill="none" stroke-width="26">
      <circle cx="65" cy="65" r="44" stroke="var(--gray)" stroke-dasharray="88 188"/>
    </g>
    <circle cx="65" cy="65" r="30" fill="var(--white)"/>
    <text x="65" y="68" text-anchor="middle" font-family="Montserrat, Arial, sans-serif" font-weight="800" font-size="9" fill="var(--ink)">LEVERAGE</text>
    <text x="36" y="30" text-anchor="middle" font-family="Montserrat, Arial, sans-serif" font-weight="600" font-size="7" fill="#fff">Network</text>
    <text x="108" y="62" text-anchor="middle" font-family="Montserrat, Arial, sans-serif" font-weight="600" font-size="7" fill="#fff">Process</text>
    <text x="56" y="118" text-anchor="middle" font-family="Montserrat, Arial, sans-serif" font-weight="600" font-size="7" fill="#fff">Experience</text>
  </svg>

  <div class="abs heading section-title" style="left:216px;top:428px">Efficient Process</div>
  <div class="step step--blue" style="left:214px;top:466px">Exploratory Call</div>
  <div class="step step--orange" style="left:260px;top:458px">Regulatory Landscape</div>
  <div class="step step--blue" style="left:306px;top:450px">Problem Statement</div>
  <div class="step step--orange" style="left:352px;top:442px">Review &amp; Align on Deliverables</div>

  <div class="abs heading section-title" style="left:216px;top:503px">Valued Partner Network</div>
  <div class="partner" style="left:218px;top:518px;width:28px;height:14px" aria-label="Partner badge"></div>
  <div class="partner" style="left:254px;top:518px;width:36px;height:14px" aria-label="Partner badge"></div>
  <div class="partner" style="left:298px;top:518px;width:36px;height:14px" aria-label="Partner badge"></div>
  <div class="partner" style="left:342px;top:518px;width:28px;height:14px" aria-label="Partner badge"></div>
  <div class="partner" style="left:378px;top:518px;width:26px;height:14px" aria-label="Partner badge"></div>

  <div class="abs contact" style="left:226px;top:541px;font-size:8px">
    <svg width="10" height="10" viewBox="0 0 24 24" aria-hidden="true"><circle cx="12" cy="12" r="11" fill="none" stroke="#fff" stroke-width="2"/><path d="M8 6l2 0 1 3-1.5 1a7 7 0 0 0 3.5 3.5l1-1.5 3 1v2a2 2 0 0 1-2 2A10 10 0 0 1 6 8a2 2 0 0 1 2-2z" fill="#fff"/></svg>
    <a href="tel:5550142290">555.014.2290</a>
  </div>
  <div class="abs contact" style="left:306px;top:542px;font-size:6.5px">
    <a href="mailto:info@halvernadvisory.com">info@halvernadvisory.com</a>
  </div>
  <a class="abs web" href="https://www.halvernadvisory.com" style="left:20px;top:572px">www.halvernadvisory.com</a>
</section>

</body>
</html>
```